Marist Valley College Brenthurst Letterhead

Our college is called Marist Valley College Brenthurst. We would like to request a few letterhead design options to choose from please. We look forward to seeing some new and fresh ideas for our College Letterhead.

Please note that the College has the following PMS Colours:
MAROON – PMS 229C
BLUE – PMS 2747C
GOLD – PMS 871C
YELLOW – PMS 123C

Our College Motto is:
Truth Guiding Learning.
I have attached a copy of our current letterhead and College Logo.

Please note that the letterhead must include the following details:

Marist Valley College Brenthurst
Truth Guiding Learning
Phone: 8472 5518
Fax:8415 7730
Address: 214 Kellaway Street Brenthurst 3041
Mail:PO BOX 4857 Marlow Heights VIC 3045 Australia
ABN 61 507 284 913

www.mvcbrenthurst-example.net
https://chatterly.example/mvcbrenthurst
https://www.pinwall.example/mvcbrenthurst
https://www.friendspace.example/MVCBrenthurst
www.vidstream.example (search MVC Brenthurst)

Please feel free to contact me on the below detail if I can further assist.

Regards,
Joanna Whitcombe
reception@mvcbrenthurst-example.net
PH: 8472 5518

Target Market(s)

College Community

Industry/Entity Type

Education

Font styles to use
Other font styles liked:
• You decide

Requirements
Must have
• See Project Description
Nice to have
• see Project Description

```html
<!DOCTYPE html>
<html lang="en">
<head>
<meta charset="utf-8">
<title>Marist Valley College Brenthurst – Letterhead Options</title>
<link rel="stylesheet" href="https://fonts.googleapis.com/css2?family=PT+Sans:wght@400;700&display=swap">
<style>
  :root {
    --maroon: #6b1f48;
    --blue: #262f6b;
    --gold: #f7c22b;
    --yellow: #ffc82e;
    --crest-red: #8e2a3c;
    --ink: #555560;
    --paper: #ffffff;
    --backdrop: #3a2a22;
  }
  * { box-sizing: border-box; margin: 0; padding: 0; }
  html, body { width: 1200px; height: 1000px; overflow: hidden; }
  body {
    background: var(--backdrop);
    font-family: "PT Sans", Arial, sans-serif;
    position: relative;
  }
  .letterhead {
    position: absolute;
    top: 180px;
    width: 490px;
    height: 640px;
    background: var(--paper);
    box-shadow: 0 6px 18px rgba(0,0,0,.45);
    overflow: hidden;
  }
  .letterhead--maroon { left: 90px; --brand: var(--maroon); }
  .letterhead--blue { left: 620px; --brand: var(--blue); }
  .header-art { position: absolute; left: 0; top: 0; width: 490px; height: 190px; }
  .header-text {
    position: absolute; left: 18px; top: 22px; right: 16px;
    display: flex; align-items: flex-start; color: #fff;
  }
  .motto { font-weight: 700; font-size: 13.5px; white-space: nowrap; padding-right: 12px; border-right: 1px solid rgba(255,255,255,.8); line-height: 18px; }
  .motto .accent { color: var(--gold); }
  .college { padding-left: 12px; text-align: right; flex: 1; }
  .college-name { color: var(--gold); font-weight: 700; font-size: 13.5px; line-height: 18px; white-space: nowrap; }
  .college-phone { font-size: 8.5px; font-weight: 700; color: var(--gold); }
  .college-phone span { color: #fff; }
  .crest-mark {
    position: absolute; right: 24px; top: 58px;
    width: 104px; height: 104px; border-radius: 50%;
    background: var(--crest-red); border: 4px solid var(--blue);
  }
  .crest-name {
    position: absolute; right: 14px; top: 168px; width: 124px;
    text-align: center; font-size: 9px; line-height: 11px;
    font-weight: 700; color: var(--brand);
  }
  .footer-divider { position: absolute; width: 1px; height: 50px; background: var(--brand); top: 560px; left: 206px; }
  .letterhead--maroon .footer-divider { left: 240px; }
  .links {
    position: absolute; right: 32px; top: 560px;
    text-align: right; font-size: 7.6px; line-height: 10px; color: var(--ink);
  }
  .links b { color: var(--brand); font-weight: 700; }
  .edge-bar { position: absolute; right: 0; top: 560px; width: 22px; height: 50px; background: var(--brand); }
  .address {
    position: absolute; left: 30px; top: 580px;
    font-size: 7.6px; line-height: 10px; color: var(--ink);
  }
  .address b { color: var(--brand); font-weight: 700; }
  .address-bar { position: absolute; left: 0; top: 580px; width: 18px; height: 50px; background: var(--yellow); }
</style>
</head>
<body>

<section class="letterhead letterhead--maroon" aria-label="Letterhead option in maroon">
  <svg class="header-art" viewBox="0 0 490 190" aria-hidden="true">
    <path d="M0 0H490V140Q290 40 0 75Z" fill="var(--maroon)"/>
    <path d="M0 75Q290 40 490 140V172Q300 58 0 84Z" fill="var(--yellow)"/>
  </svg>
  <div class="header-text">
    <p class="motto">Truth <span class="accent">Guiding</span> Learning</p>
    <div class="college">
      <p class="college-name">Marist Valley College Brenthurst</p>
      <p class="college-phone">Phone : <span>8472 5518</span> | Fax : <span>8415 7730</span></p>
    </div>
  </div>
  <div class="crest-mark" aria-hidden="true"></div>
  <p class="crest-name">Marist Valley College</p>

  <div class="address-bar"></div>
  <p class="address">
    <b>Address</b> : 214 Kellaway Street<br>
    Brenthurst 3041<br>
    <b>Mail</b> : PO BOX 4857 Marlow Heights<br>
    VIC 3045 Australia<br>
    <b>ABN 61 507 284 913</b>
  </p>
  <div class="footer-divider"></div>
  <p class="links">
    www.<b>mvcbrenthurst-example</b>.net<br>
    https://<b>chatterly</b>.example/mvcbrenthurst<br>
    https://www.<b>pinwall</b>.example/mvcbrenthurst<br>
    https://www.<b>friendspace</b>.example/MVCBrenthurst<br>
    www.<b>vidstream</b>.example (search MVC Brenthurst)
  </p>
  <div class="edge-bar"></div>
</section>

<section class="letterhead letterhead--blue" aria-label="Letterhead option in blue">
  <svg class="header-art" viewBox="0 0 490 190" aria-hidden="true">
    <path d="M0 0H490V140Q290 40 0 75Z" fill="var(--blue)"/>
    <path d="M0 75Q290 40 490 140V172Q300 58 0 84Z" fill="var(--yellow)"/>
  </svg>
  <div class="header-text">
    <p class="motto">Truth <span class="accent">Guiding</span> Learning</p>
    <div class="college">
      <p class="college-name">Marist Valley College Brenthurst</p>
      <p class="college-phone">Phone : <span>8472 5518</span> | Fax : <span>8415 7730</span></p>
    </div>
  </div>
  <div class="crest-mark" aria-hidden="true"></div>
  <p class="crest-name">Marist Valley College</p>

  <div class="footer-divider"></div>
  <p class="links">
    www.<b>mvcbrenthurst-example</b>.net<br>
    https://<b>chatterly</b>.example/mvcbrenthurst<br>
    https://www.<b>pinwall</b>.example/mvcbrenthurst<br>
    https://www.<b>friendspace</b>.example/MVCBrenthurst<br>
    www.<b>vidstream</b>.example (search MVC Brenthurst)
  </p>
  <div class="edge-bar"></div>
</section>

</body>
</html>
```